BrimKeel conversion company design.

Hi,

We specialise in attic/roof conversions to create more space. We have a logo design which we are happy with. We would like someone to design a wrap that will be suitable to be transferred onto a 2008 Corva 310. This is our first car to be wrapped and is what we require a design for.

However, we would like to see a design that can be utilised on a KT Selvano, and 2021 Marelle Haulan van. (I understand the design would change to suit but I would like something that will still look similar when they are sat next to one another).

We have a white background on the car so that would need consideration.

We want something that is noticeable but looks professional.

We will also require are contact information on the design:

email: admin@brimkeel.com.au
Website: brimkeel.com.au
Tel: 1300847162
Social media icons- Glimmora, Kindlyst, Tacklore, Zelvo

Please let me know if you require any further detail.

```html
<!DOCTYPE html>
<html lang="en">
<head>
<meta charset="utf-8">
<title>BrimKeel Vehicle Wrap</title>
<link rel="stylesheet" href="https://fonts.googleapis.com/css2?family=Montserrat:wght@500;600;700&family=Catamaran:wght@500&display=swap">
<style>
  :root {
    --wrap-blue: #2f7dcb;
    --brand-blue: #1d6cb6;
    --charcoal: #2a3038;
    --white: #ffffff;
    --page: #eef0f3;
    --edge: #d9dde3;
  }
  * { box-sizing: border-box; margin: 0; padding: 0; }
  html, body { width: 1200px; height: 1200px; overflow: hidden; }
  body {
    background: var(--page);
    font-family: "Montserrat", Arial, sans-serif;
    position: relative;
  }
  .wrap-panel {
    position: absolute;
    left: 50px;
    width: 1100px;
    height: 350px;
    background: var(--white);
    border: 1px solid var(--edge);
    overflow: hidden;
  }
  .wrap-panel--pickup { top: 30px; }
  .wrap-panel--hatch  { top: 425px; }
  .wrap-panel--van    { top: 820px; }
  .wrap-graphic {
    position: absolute;
    inset: 0;
    width: 100%;
    height: 100%;
  }
  .wrap-graphic .blue-field { fill: var(--wrap-blue); }
  .wrap-graphic .dark-stripe { fill: var(--charcoal); }

  .brand-block {
    position: absolute;
    top: 62px;
    width: 420px;
    text-align: center;
  }
  .brand-mark {
    width: 22px;
    height: 22px;
    background: var(--brand-blue);
    margin: 0 auto 14px;
  }
  .brand-name {
    font-family: "Montserrat", Arial, sans-serif;
    font-weight: 600;
    font-size: 56px;
    letter-spacing: 1px;
    color: var(--brand-blue);
    line-height: 1;
  }
  .brand-tagline {
    font-family: "Catamaran", Arial, sans-serif;
    font-weight: 500;
    font-size: 18px;
    color: var(--charcoal);
    margin-top: 12px;
  }
  .brand-rule {
    width: 130px;
    height: 3px;
    background: var(--brand-blue);
    margin: 10px auto 0;
  }
  .brand-web {
    font-family: "Montserrat", Arial, sans-serif;
    font-weight: 500;
    font-size: 26px;
    color: var(--brand-blue);
    margin-top: 22px;
    letter-spacing: 1px;
  }

  .contact-block {
    position: absolute;
    top: 48px;
    right: 50px;
    text-align: right;
    color: var(--white);
  }
  .contact-email {
    display: flex;
    align-items: center;
    justify-content: flex-end;
    gap: 10px;
    font-weight: 500;
    font-size: 24px;
  }
  .contact-email svg { width: 22px; height: 18px; }
  .contact-phone {
    font-weight: 700;
    font-size: 46px;
    letter-spacing: 1px;
    margin-top: 6px;
  }
  .social-row {
    display: flex;
    justify-content: flex-end;
    gap: 14px;
    margin-top: 22px;
    font-weight: 600;
    font-size: 15px;
  }
  .social-item { display: flex; align-items: center; gap: 6px; }
  .social-dot {
    width: 10px;
    height: 10px;
    border-radius: 50%;
    background: var(--white);
  }
</style>
</head>
<body>

  <section class="wrap-panel wrap-panel--pickup" aria-label="BrimKeel wrap for KT Selvano">
    <svg class="wrap-graphic" viewBox="0 0 1100 350" preserveAspectRatio="none" aria-hidden="true">
      <polygon class="dark-stripe" points="655,0 675,0 525,350 505,350"/>
      <polygon class="blue-field" points="690,0 1100,0 1100,350 540,350"/>
    </svg>
    <div class="brand-block" style="left:60px;">
      <div class="brand-mark"></div>
      <div class="brand-name">BrimKeel</div>
      <div class="brand-tagline">Storage • Skylights • Conversions</div>
      <div class="brand-rule"></div>
      <div class="brand-web">brimkeel.com.au</div>
    </div>
    <div class="contact-block">
      <div class="contact-email">
        <svg viewBox="0 0 22 18" aria-hidden="true"><rect x="1" y="1" width="20" height="16" rx="2" fill="none" stroke="#fff" stroke-width="2"/><polyline points="2,3 11,10 20,3" fill="none" stroke="#fff" stroke-width="2"/></svg>
        admin@brimkeel.com.au
      </div>
      <div class="contact-phone">1300847162</div>
      <div class="social-row">
        <span class="social-item"><span class="social-dot"></span>Kindlyst</span>
        <span class="social-item"><span class="social-dot"></span>Zelvo</span>
        <span class="social-item"><span class="social-dot"></span>Glimmora</span>
        <span class="social-item"><span class="social-dot"></span>Tacklore</span>
      </div>
    </div>
  </section>

  <section class="wrap-panel wrap-panel--hatch" aria-label="BrimKeel wrap for Corva 310">
    <svg class="wrap-graphic" viewBox="0 0 1100 350" preserveAspectRatio="none" aria-hidden="true">
      <polygon class="dark-stripe" points="620,0 640,0 470,350 450,350"/>
      <polygon class="blue-field" points="655,0 1100,0 1100,350 485,350"/>
    </svg>
    <div class="brand-block" style="left:40px;">
      <div class="brand-mark"></div>
      <div class="brand-name">BrimKeel</div>
      <div class="brand-tagline">Storage • Skylights • Conversions</div>
      <div class="brand-rule"></div>
      <div class="brand-web">brimkeel.com.au</div>
    </div>
    <div class="contact-block">
      <div class="contact-email">
        <svg viewBox="0 0 22 18" aria-hidden="true"><rect x="1" y="1" width="20" height="16" rx="2" fill="none" stroke="#fff" stroke-width="2"/><polyline points="2,3 11,10 20,3" fill="none" stroke="#fff" stroke-width="2"/></svg>
        admin@brimkeel.com.au
      </div>
      <div class="contact-phone">1300847162</div>
      <div class="social-row">
        <span class="social-item"><span class="social-dot"></span>Kindlyst</span>
        <span class="social-item"><span class="social-dot"></span>Zelvo</span>
        <span class="social-item"><span class="social-dot"></span>Glimmora</span>
        <span class="social-item"><span class="social-dot"></span>Tacklore</span>
      </div>
    </div>
  </section>

  <section class="wrap-panel wrap-panel--van" aria-label="BrimKeel wrap for Marelle Haulan">
    <svg class="wrap-graphic" viewBox="0 0 1100 350" preserveAspectRatio="none" aria-hidden="true">
      <polygon class="dark-stripe" points="640,0 660,0 470,350 450,350"/>
      <polygon class="blue-field" points="675,0 1100,0 1100,350 485,350"/>
    </svg>
    <div class="brand-block" style="left:50px;">
      <div class="brand-mark"></div>
      <div class="brand-name">BrimKeel</div>
      <div class="brand-tagline">Storage • Skylights • Conversions</div>
      <div class="brand-rule"></div>
      <div class="brand-web">brimkeel.com.au</div>
    </div>
    <div class="contact-block">
      <div class="contact-email">
        <svg viewBox="0 0 22 18" aria-hidden="true"><rect x="1" y="1" width="20" height="16" rx="2" fill="none" stroke="#fff" stroke-width="2"/><polyline points="2,3 11,10 20,3" fill="none" stroke="#fff" stroke-width="2"/></svg>
        admin@brimkeel.com.au
      </div>
      <div class="contact-phone">1300847162</div>
      <div class="social-row">
        <span class="social-item"><span class="social-dot"></span>Kindlyst</span>
        <span class="social-item"><span class="social-dot"></span>Zelvo</span>
        <span class="social-item"><span class="social-dot"></span>Glimmora</span>
        <span class="social-item"><span class="social-dot"></span>Tacklore</span>
      </div>
    </div>
  </section>

</body>
</html>
```